lawn sign

Lawn Sign
Roofing Gutters Windows

Target Market(s)

roofing

Font styles to use
Sans Serif

Colors
86cfc6
33a6d7
fbee3f
faa54b

Requirements
Must have
• my logo
Nice to have
• designer for now

```html
<!DOCTYPE html>
<html lang="en">
<head>
<meta charset="utf-8">
<title>Lawn Sign Samples</title>
<link href="https://fonts.googleapis.com/css2?family=Roboto+Condensed:ital,wght@0,400;0,700;1,700&display=swap" rel="stylesheet">
<style>
  :root{
    --backdrop:#555759;
    --white:#ffffff;
    --navy:#15457f;
    --blue:#1f6db3;
    --blue-dark:#134f8e;
    --green:#4f9a2c;
    --green-light:#7cbf3a;
    --grey-panel:#e4e6e8;
    --label:#1c3f6e;
    --sky:#9cc3e0;
    --house:#6d5a4c;
  }
  *{box-sizing:border-box;margin:0;padding:0}
  html,body{width:1200px;height:2336px;overflow:hidden;background:var(--backdrop);font-family:"Roboto Condensed",sans-serif}
  .canvas{position:relative;width:1200px;height:2336px}
  .sign{position:absolute;left:88px;width:960px;background:var(--white);overflow:hidden}
  .sample-tag{position:absolute;left:1088px;color:#f2f2f2;font-size:34px;letter-spacing:3px;transform:rotate(90deg);transform-origin:left top;white-space:nowrap}
  .photo{position:absolute;background:linear-gradient(180deg,var(--sky) 0%,#c9d8c4 35%,var(--house) 62%,#b9b4a8 100%)}
  .service{position:absolute;width:200px;text-align:center}
  .service .badge{width:180px;height:180px;margin:0 auto;border-radius:50%;background:var(--green);border:6px solid var(--white);display:flex;align-items:center;justify-content:center}
  .service .badge svg{width:96px;height:96px}
  .service .name{margin-top:10px;font-weight:700;font-size:36px;color:var(--label)}
  .brand{position:absolute;display:flex;align-items:center;gap:22px}
  .brand .dot{border-radius:50%;background:var(--green-light)}
  .brand .word{color:var(--blue);font-weight:400;line-height:1.05}
  .phone{position:absolute;color:var(--white);font-weight:700;font-style:italic;white-space:nowrap}
  .url{position:absolute;background:var(--green);color:var(--white);font-weight:700;display:flex;align-items:center;justify-content:center;letter-spacing:1px}
  .bar{position:absolute;background:linear-gradient(180deg,var(--blue),var(--blue-dark))}
  /* sample 2 side column */
  .side{position:absolute;background:var(--grey-panel)}
  .side .service{width:240px}
  .side .service .badge{width:130px;height:130px}
  .side .service .badge svg{width:70px;height:70px}
  .side .service .name{font-size:26px;margin-top:4px}
</style>
</head>
<body>
<svg width="0" height="0" style="position:absolute">
  <symbol id="icon-roof" viewBox="0 0 100 100"><path d="M50 14 L92 50 L82 50 L50 24 L18 50 L8 50 Z" fill="#fff"/><path d="M24 52 L50 30 L76 52 L76 84 L58 84 L58 62 L42 62 L42 84 L24 84 Z" fill="#fff"/></symbol>
  <symbol id="icon-window" viewBox="0 0 100 100"><rect x="16" y="16" width="31" height="31" fill="#fff"/><rect x="53" y="16" width="31" height="31" fill="#fff"/><rect x="16" y="53" width="31" height="31" fill="#fff"/><rect x="53" y="53" width="31" height="31" fill="#fff"/></symbol>
  <symbol id="icon-gutter" viewBox="0 0 100 100"><path d="M10 22 H90 V34 Q90 50 74 50 H62 V88 H46 V50 H26 Q10 50 10 34 Z" fill="#fff"/><rect x="16" y="28" width="68" height="6" fill="#4f9a2c"/></symbol>
</svg>

<main class="canvas">

  <!-- Sample 1 -->
  <section class="sign" style="top:72px;height:680px">
    <div class="photo" role="img" aria-label="Photo of a Tudor-style house with a conservatory" style="left:0;top:0;width:960px;height:400px"></div>
    <div class="service" style="left:32px;top:210px"><div class="badge"><svg><use href="#icon-roof"/></svg></div><div class="name">ROOFING</div></div>
    <div class="service" style="left:372px;top:210px"><div class="badge"><svg><use href="#icon-window"/></svg></div><div class="name">WINDOWS</div></div>
    <div class="service" style="left:712px;top:210px"><div class="badge"><svg><use href="#icon-gutter"/></svg></div><div class="name">GUTTERS</div></div>
    <div class="brand" style="left:28px;top:500px"><span class="dot" style="width:90px;height:90px"></span><span class="word" style="font-size:28px">HARLOW<br>Restoration<br>Remodeling Group LLC</span></div>
    <div class="bar" style="left:400px;top:490px;width:560px;height:110px"></div>
    <div class="phone" style="left:420px;top:494px;font-size:86px">(555) 014-7720</div>
    <div class="url" style="left:400px;top:600px;width:560px;height:60px;font-size:40px">WWW.HARLOWLLC.COM</div>
  </section>
  <div class="sample-tag" style="top:300px">SAMPLE 1</div>

  <!-- Sample 2 -->
  <section class="sign" style="top:832px;height:668px">
    <div class="brand" style="left:36px;top:30px"><span class="dot" style="width:150px;height:150px"></span><span class="word" style="font-size:44px">HARLOW<br>Restoration<br>Remodeling Group LLC</span></div>
    <div class="photo" role="img" aria-label="Photo of a Tudor-style house with a conservatory" style="left:0;top:230px;width:720px;height:310px"></div>
    <div class="side" style="left:720px;top:0;width:240px;height:540px">
      <div class="service" style="left:0;top:14px"><div class="badge"><svg><use href="#icon-roof"/></svg></div><div class="name">ROOFING</div></div>
      <div class="service" style="left:0;top:190px"><div class="badge"><svg><use href="#icon-window"/></svg></div><div class="name">WINDOWS</div></div>
      <div class="service" style="left:0;top:366px"><div class="badge"><svg><use href="#icon-gutter"/></svg></div><div class="name">GUTTERS</div></div>
    </div>
    <div class="bar" style="left:0;top:540px;width:960px;height:128px"></div>
    <div class="phone" style="left:28px;top:552px;font-size:84px">(555) 014-7720</div>
    <div class="url" style="left:556px;top:568px;width:384px;height:70px;font-size:36px">WWW.HARLOWLLC.COM</div>
  </section>
  <div class="sample-tag" style="top:1060px">SAMPLE 2</div>

  <!-- Sample 3 -->
  <section class="sign" style="top:1600px;height:660px;border:8px solid var(--blue)">
    <div class="brand" style="left:40px;top:36px"><span class="dot" style="width:170px;height:170px"></span><span class="word" style="font-size:54px">HARLOW<br>Restoration<br>Remodeling Group LLC</span></div>
    <div class="side" style="left:0;top:270px;width:944px;height:262px"></div>
    <div class="service" style="left:60px;top:290px"><div class="badge"><svg><use href="#icon-roof"/></svg></div><div class="name">ROOFING</div></div>
    <div class="service" style="left:372px;top:290px"><div class="badge"><svg><use href="#icon-window"/></svg></div><div class="name">WINDOWS</div></div>
    <div class="service" style="left:684px;top:290px"><div class="badge"><svg><use href="#icon-gutter"/></svg></div><div class="name">GUTTERS</div></div>
    <div class="bar" style="left:0;top:532px;width:944px;height:112px"></div>
    <div class="phone" style="left:22px;top:538px;font-size:80px">(555) 014-7720</div>
    <div class="url" style="left:540px;top:556px;width:384px;height:66px;font-size:36px">WWW.HARLOWLLC.COM</div>
  </section>
  <div class="sample-tag" style="top:1820px">SAMPLE 3</div>

</main>
</body>
</html>
```